Metal head/ Sushi chef wanting artistic yet high imact business card

I'm sushi chef for make living in Australia originally from Tokyo Japan.
I'm also guitarist/composer as well on progressive metalcore/djent genre.
My favorite visual art is Mandala. Sacred geometries, Fractals, Paisleys are also things fit in me. I like dark color, earth color, and sometimes psychedelic patterns.
I want to hand out my business card when I meet new people in music industries or someone who is wanting private sushi chef for their party.
I know metal and sushi are far different subjects but they are all my passion. I would like to work with the designer who can create something cool from information above.

https://www.vidlorix.com/channel/QX8p4LtRwe7JnVb2kHs9DY3m
https://tunebarrel.com/user-804716273

Front
my name, Haruki Motobe
occupation, "Sushi chef" "Metal guitarist/composer"
Email address, pelvonmist@tavemail.net
Phone number, (61)498201753

Back:
My Vidlorix channel, Friendquay, Tunebarrel, Pictavio. All of those are searchable by "Pelvonmist" The website mentioned above can be described as their logos.

Target Market(s)

people in Music industry, such as musicians, venue managers, promoters.
People who wants to have private sushi chef for their private function, party or events.

Industry/Entity Type

Artists

Contact Information for Business Card

Uploaded photos are just image reference. not thinking to use them.
My details:
I like :
energetic music that has a lot of details such as Progressive metalcore, jazz, djent, psychedelic music.
Spiritual thoughs, Buddism, fundamentals, relaxation music, 420, weed culture, Free thoughts
U.S street culture, skate board, brelks, surf, bicycle, nature, camping, hiking, ocean, mountain, desert, countryside,
permaculture, natural farming, organic farming, compost, self sufficient.
nigiri sushi, art sushi, something/someone beautiful in mind.

Dislike:
Fakes, Bullshits, format, negative, preservatives, artificial colors, illuminati, satanism, manipulation, mass favorites, big society, politics, Chinese letters on western design

Colors
0455a3
000000
7c7c7c
00a990
acd036
f37122

Requirements
Must have
• Front
• my name, Haruki Motobe
• occupation, "Sushi chef" "Metal guitarist/composer"
• Email address, pelvonmist@tavemail.net
• Phone number, (61)498201753
• Back:
• My Vidlorix channel, Friendquay, Tunebarrel, Pictavio. All of those are searchable by "Pelvonmist" The website mentioned above can be described as their logos.
Nice to have
• something based on one of those either back ground or logo:
• Mandala, Sacred Geometry, Fractal art
Should not have
• pop essence. mass favorites, pink, Chinese letters, asian fonts, something asian

```html
<!DOCTYPE html>
<html lang="en">
<head>
<meta charset="utf-8">
<title>Haruki Motobe — Business Card</title>
<link href="https://fonts.googleapis.com/css2?family=Lato:wght@400;700&display=swap" rel="stylesheet">
<style>
  :root {
    --backdrop: #3a3330;
    --card-black: #0b0b0b;
    --card-black-soft: #151515;
    --text-white: #ffffff;
    --text-grey: #b9b9b9;
    --social-blue: #3a63a8;
    --flare-red: #b52a0e;
    --flare-orange: #f37122;
    --flare-dark: #4a0c04;
  }
  * { margin: 0; padding: 0; box-sizing: border-box; }
  html, body {
    width: 1200px; height: 844px; overflow: hidden;
    background: var(--backdrop);
    font-family: "Lato", sans-serif;
  }
  .stage {
    width: 1200px; height: 844px;
    display: flex; align-items: center; justify-content: center; gap: 40px;
  }
  .card {
    position: relative;
    width: 520px; height: 297px;
    background: linear-gradient(135deg, var(--card-black-soft), var(--card-black));
    overflow: hidden;
    box-shadow: 0 10px 30px rgba(0,0,0,0.45);
  }
  /* Front */
  .portrait {
    position: absolute;
    left: -70px; top: -8px;
    width: 313px; height: 313px;
    border-radius: 50%;
    background: radial-gradient(circle at 55% 35%, var(--flare-orange) 0%, var(--flare-red) 40%, var(--flare-dark) 85%);
  }
  .identity {
    position: absolute;
    right: 34px; top: 78px;
    text-align: right;
    color: var(--text-grey);
    font-size: 14px;
    line-height: 1.55;
  }
  .identity .name {
    color: var(--text-white);
    font-weight: 700;
    font-size: 19px;
    letter-spacing: 0.5px;
    text-transform: uppercase;
    line-height: 1.3;
  }
  .identity .role { font-size: 13.5px; }
  .identity .contact {
    margin-top: 8px;
    display: flex; justify-content: flex-end; align-items: center; gap: 6px;
    color: var(--text-white);
    font-size: 14px;
  }
  .identity .contact + .contact { margin-top: 0; }
  .contact svg { width: 13px; height: 13px; fill: var(--text-white); flex-shrink: 0; }
  /* Back */
  .pattern {
    position: absolute; inset: 0;
    background: radial-gradient(circle at 40% 40%, #1a1a1a, #0a0a0a 75%);
  }
  .socials {
    position: absolute; left: 0; right: 0; top: 110px;
    text-align: center;
    color: var(--text-white);
    font-size: 13px;
  }
  .socials .networks { display: flex; justify-content: center; gap: 14px; margin-bottom: 4px; }
  .socials .network { display: flex; align-items: center; gap: 5px; }
  .socials .dot { width: 12px; height: 12px; border-radius: 50%; background: var(--social-blue); }
  .socials .handle { margin-bottom: 22px; }
  .socials .url { font-size: 13px; line-height: 1.6; letter-spacing: 0.2px; }
</style>
</head>
<body>
<main class="stage">
  <section class="card card-front">
    <div class="portrait" role="img" aria-label="Portrait photo of the guitarist in front of a fiery red-orange solar flare"></div>
    <div class="identity">
      <div class="name">Haruki Motobe</div>
      <div class="role">Sushi chef</div>
      <div class="role">Metal guitarist/composer</div>
      <div class="contact">(61)498201753
        <svg viewBox="0 0 16 16" aria-hidden="true"><path d="M1 5c2-3 12-3 14 0v2h-4V5.5C9.5 5 6.5 5 5 5.5V7H1z M4 8h8l2 6H2z"/></svg>
      </div>
      <div class="contact">pelvonmist@tavemail.net
        <svg viewBox="0 0 16 16" aria-hidden="true"><path d="M1 3h14v10H1z" fill="none" stroke="#fff" stroke-width="1.5"/><path d="M1 3l7 6 7-6" fill="none" stroke="#fff" stroke-width="1.5"/></svg>
      </div>
    </div>
  </section>

  <section class="card card-back">
    <div class="pattern" role="img" aria-label="Faint dark geometric star-lattice pattern"></div>
    <div class="socials">
      <div class="networks">
        <span class="network"><span class="dot"></span>Friendquay</span>
        <span class="network"><span class="dot"></span>Pictavio</span>
      </div>
      <div class="handle">Pelvonmist</div>
      <div class="url">www.vidlorix.com/channel/QX8p4LtRwe7JnVb2kHs9DY3m</div>
      <div class="url">www.tunebarrel.com/user-804716273</div>
    </div>
  </section>
</main>
</body>
</html>
```